Textbook cover for dental seminar

I'm looking for a fresh new design for our annual textbook. You will need to incorporate our logo, business name (BeccaCDT's Dental Hygiene Institute) - the words "BeccaCDT's" needs to be larger or the same size as "Dental Hygiene Academy" and colors of dentistry is purple so I like to stick with shades of purple in the design however it does not need to be all purple or only purple. The words "with hygiene career booster" will not be on next years edition so please do not add that. The book will have spiral binding so please account for that when designing. Please see our website for information BeccaCDTExamPrep.example
Updates

I also want listed on the cover somewhere “The World’s First Interactive Review Book!”

Size will be 8.5" x 11"

```html
<!DOCTYPE html>
<html lang="en">
<head>
<meta charset="utf-8">
<title>BeccaCDT's Dental Hygiene Institute – Cover</title>
<link href="https://fonts.googleapis.com/css2?family=Montserrat:wght@700;800&display=swap" rel="stylesheet">
<style>
  :root {
    --stage: #8a97a1;
    --cover-purple: #8b2a8a;
    --deep-violet: #220c4f;
    --ink-navy: #1f0f4b;
    --ribbon-purple: #8b2a8b;
    --white: #ffffff;
    --badge-black: #111111;
    --seal-lilac: #7a3a9a;
  }
  html, body {
    margin: 0;
    width: 808px;
    height: 1200px;
    overflow: hidden;
    background: var(--stage);
  }
  .cover {
    position: absolute;
    left: 0;
    top: 77px;
    width: 808px;
    height: 1046px;
    background: var(--cover-purple);
    overflow: hidden;
    font-family: "Montserrat", sans-serif;
  }
  .cover-shapes {
    position: absolute;
    inset: 0;
  }
  .site-url {
    position: absolute;
    left: 74px;
    top: 946px;
    transform-origin: 0 0;
    transform: rotate(-90deg);
    margin: 0;
    color: var(--white);
    font-weight: 800;
    font-size: 31px;
    letter-spacing: 3.6px;
    white-space: nowrap;
    line-height: 1;
  }
  .ribbon-text {
    position: absolute;
    left: 548px;
    top: 36px;
    width: 260px;
    margin: 0;
    text-align: center;
    font-weight: 800;
    line-height: 1.05;
  }
  .ribbon-text .accent { color: var(--ribbon-purple); font-size: 24px; display: block; }
  .ribbon-text .strong { color: var(--ink-navy); font-size: 33px; display: block; }
  .title {
    position: absolute;
    left: 137px;
    top: 360px;
    margin: 0;
    color: var(--white);
    font-weight: 800;
    font-size: 68px;
    line-height: 67px;
    letter-spacing: 0.5px;
  }
  .title span { display: block; }
  .seal-name {
    position: absolute;
    left: 290px;
    top: 790px;
    width: 214px;
    margin: 0;
    text-align: center;
    color: var(--white);
    font-weight: 800;
    font-size: 19px;
    line-height: 1.2;
  }
  .app-cta {
    position: absolute;
    left: 136px;
    top: 953px;
  }
  .app-cta-label {
    margin: 0 0 6px;
    color: var(--white);
    font-weight: 800;
    font-size: 23px;
    line-height: 1;
  }
  .store-badges { display: flex; gap: 7px; }
  .store-badge {
    width: 98px;
    height: 30px;
    box-sizing: border-box;
    border: 1.5px solid #888;
    border-radius: 5px;
    background: var(--badge-black);
    color: var(--white);
    font-weight: 700;
    font-size: 13px;
    display: flex;
    align-items: center;
    justify-content: center;
  }
  .tagline {
    position: absolute;
    right: 30px;
    top: 955px;
    width: 330px;
    margin: 0;
    text-align: right;
    color: var(--white);
    font-weight: 800;
    font-size: 21px;
    line-height: 1.25;
  }
</style>
</head>
<body>
<main class="cover">
  <svg class="cover-shapes" width="808" height="1046" viewBox="0 0 808 1046" aria-hidden="true">
    <defs>
      <linearGradient id="waveGlow" x1="0" y1="0" x2="1" y2="1">
        <stop offset="0" stop-color="#c77fd0" stop-opacity="0.1"/>
        <stop offset="0.5" stop-color="#e8c6ee" stop-opacity="0.35"/>
        <stop offset="1" stop-color="#c77fd0" stop-opacity="0.12"/>
      </linearGradient>
      <linearGradient id="blobShade" x1="0" y1="0" x2="1" y2="1">
        <stop offset="0" stop-color="#2a0f5a"/>
        <stop offset="1" stop-color="#4a1a78"/>
      </linearGradient>
    </defs>
    <ellipse class="blob-tail" cx="250" cy="760" rx="150" ry="85" fill="url(#blobShade)"/>
    <circle class="hero-disc" cx="417" cy="528" r="318" fill="var(--deep-violet)"/>
    <path class="wave-field" role="img" aria-label="Flowing fine-line wave decoration"
          d="M808 300 C 700 520, 640 640, 720 760 C 790 870, 620 960, 560 1046 L 808 1046 Z"
          fill="url(#waveGlow)"/>
    <circle class="ring-accent" cx="236" cy="247" r="47" fill="none" stroke="var(--white)" stroke-width="3"/>
    <circle class="dot-accent" cx="286" cy="214" r="29" fill="var(--white)"/>
    <circle class="seal-disc" cx="397" cy="768" r="134" fill="var(--seal-lilac)" stroke="var(--white)" stroke-width="4"/>
    <circle class="seal-mark" cx="397" cy="735" r="22" fill="var(--white)"/>
    <path class="ribbon" d="M548 0 H808 V200 L548 230 Z" fill="var(--white)"/>
  </svg>

  <p class="site-url">WWW.BECCACDTEXAMPREP.EXAMPLE</p>

  <p class="ribbon-text">
    <span class="accent">The Nations'</span>
    <span class="strong">#1 LIVE or</span>
    <span class="strong">ONLINE</span>
    <span class="accent">Board Review</span>
    <span class="accent">Seminar!</span>
  </p>

  <h1 class="title">
    <span>BECCACDT'S</span>
    <span>DENTAL</span>
    <span>HYGIENE</span>
    <span>INSTITUTE</span>
  </h1>

  <p class="seal-name">BeccaCDT's Dental Hygiene Institute</p>

  <div class="app-cta">
    <p class="app-cta-label">GET APP AN</p>
    <div class="store-badges">
      <span class="store-badge">PlayShelf</span>
      <span class="store-badge">AppVault</span>
    </div>
  </div>

  <p class="tagline">The World’s First Interactive<br>Review Book!</p>
</main>
</body>
</html>
```